Marlow Summit Holdings, LLC

I need a new business card desperately.

Please update my business card. I am looking for a professional modern classy design like the Brightfen Partners card in the attachments.

Industry/Entity Type

Investment

Contact Information for Business Card

Colors

Designer to choose colors to be used in the design.

```html
<!DOCTYPE html>
<html lang="en">
<head>
<meta charset="utf-8">
<title>Marlow Summit Holdings – Business Card</title>
<link rel="stylesheet" href="https://fonts.googleapis.com/css2?family=Oswald:wght@500;600&family=Open+Sans:wght@400;600&family=Source+Serif+4:wght@600&display=swap">
<style>
  :root {
    --brand-blue: #216db8;
    --card-grey: #eeeef0;
    --ink: #161314;
    --ink-soft: #3b3b3d;
    --white: #ffffff;
  }
  * { box-sizing: border-box; margin: 0; padding: 0; }
  html, body { width: 1200px; height: 1200px; overflow: hidden; background: var(--white); }
  .sheet { position: relative; width: 1200px; height: 1200px; }

  .card { position: absolute; left: 139px; width: 923px; height: 553px; background: var(--card-grey); overflow: hidden; }
  .card--front { top: 34px; }
  .card--back { top: 612px; }

  .top-band { position: absolute; left: 0; top: 0; width: 100%; height: 30px; background: var(--brand-blue); }

  .person-name {
    position: absolute; left: 36px; top: 38px;
    font-family: "Oswald", sans-serif; font-weight: 600; font-size: 112px; line-height: 1;
    color: var(--brand-blue); letter-spacing: -1px;
  }
  .person-title {
    position: absolute; left: 92px; top: 162px;
    font-family: "Open Sans", sans-serif; font-weight: 400; font-size: 26px;
    letter-spacing: 9px; color: var(--ink);
  }
  .person-title b { font-weight: 600; }
  .title-rule { position: absolute; left: 38px; top: 206px; width: 522px; height: 1px; background: var(--ink); }

  .company {
    position: absolute; display: flex; align-items: center; gap: 22px;
  }
  .company__mark { background: var(--ink); flex: none; }
  .company__name {
    font-family: "Oswald", sans-serif; font-weight: 600; color: var(--ink);
    text-transform: uppercase; line-height: 1.05;
  }
  .card--front .company { left: 36px; top: 262px; }
  .card--front .company__mark { width: 30px; height: 30px; }
  .card--front .company__name { font-size: 46px; letter-spacing: 3px; }

  .address {
    position: absolute; left: 80px; top: 398px;
    font-family: "Source Serif 4", serif; font-weight: 600; font-size: 22px;
    line-height: 32px; letter-spacing: 2px; color: var(--ink);
  }

  .contact-band {
    position: absolute; left: 0; bottom: 0; width: 100%; height: 59px;
    background: var(--brand-blue); color: var(--white);
    display: flex; align-items: center; padding-left: 36px;
  }
  .contact-item { display: flex; align-items: center; }
  .contact-icon { width: 38px; height: 38px; flex: none; margin-right: 10px; }
  .contact-phone { font-family: "Source Serif 4", serif; font-weight: 600; font-size: 34px; letter-spacing: 3px; }
  .contact-phone small { font-size: 12px; letter-spacing: 1px; margin-left: 8px; }
  .contact-email { margin-left: 54px; font-family: "Open Sans", sans-serif; font-weight: 600; font-size: 23px; letter-spacing: 2px; }

  .card--back .company { left: 60px; top: 120px; }
  .card--back .company__mark { width: 56px; height: 56px; }
  .card--back .company__name { font-size: 92px; letter-spacing: 8px; }
  .bottom-band { position: absolute; left: 0; bottom: 0; width: 100%; height: 137px; background: var(--brand-blue); }
</style>
</head>
<body>
<main class="sheet">
  <section class="card card--front" aria-label="Business card front">
    <div class="top-band"></div>
    <h1 class="person-name">Grant E. Marlow</h1>
    <p class="person-title"><b>M</b>anaging <b>P</b>artner</p>
    <div class="title-rule"></div>

    <div class="company">
      <span class="company__mark"></span>
      <span class="company__name">Marlow Summit<br>Holdings</span>
    </div>

    <address class="address">4217 Alder Crest Road<br>Fairhaven, TX 78900</address>

    <div class="contact-band">
      <div class="contact-item">
        <svg class="contact-icon" viewBox="0 0 38 38" aria-hidden="true">
          <circle cx="19" cy="19" r="18" fill="#ffffff"/>
          <rect x="13" y="9" width="12" height="20" rx="2" fill="none" stroke="#216db8" stroke-width="2.4"/>
          <line x1="17" y1="25.5" x2="21" y2="25.5" stroke="#216db8" stroke-width="2"/>
        </svg>
        <span class="contact-phone">555.014.2290<small>DIRECT</small></span>
      </div>
      <div class="contact-item contact-email">
        <svg class="contact-icon" viewBox="0 0 38 38" aria-hidden="true">
          <circle cx="19" cy="19" r="18" fill="#ffffff"/>
          <rect x="9" y="12" width="20" height="14" fill="none" stroke="#216db8" stroke-width="2.2"/>
          <polyline points="9,12 19,20 29,12" fill="none" stroke="#216db8" stroke-width="2.2"/>
          <line x1="9" y1="26" x2="16" y2="18" stroke="#216db8" stroke-width="1.8"/>
          <line x1="29" y1="26" x2="22" y2="18" stroke="#216db8" stroke-width="1.8"/>
        </svg>
        <span>gmarlow@msummitholdings.com</span>
      </div>
    </div>
  </section>

  <section class="card card--back" aria-label="Business card back">
    <div class="company">
      <span class="company__mark"></span>
      <span class="company__name">Marlow Summit<br>Holdings</span>
    </div>
    <div class="bottom-band"></div>
  </section>
</main>
</body>
</html>
```